VMR business card

Need a business card for a company that provides instructional design and elearning development services. The website is here: http://vantmoro.studio/

I'm attaching a current logo, as well as the old business card design. While I like to keep it clean, the old design is too simplistic for my liking. The only idea I want to reuse from the old design is placing industry jargon on the back of the card, just need a better way to present it. But if you have other ideas for the back--feel free to experiment.

Please use the colors complementary to the color we have on the website. Thank you!

```html
<!DOCTYPE html>
<html lang="en">
<head>
<meta charset="utf-8">
<title>VMR business card</title>
<link href="https://fonts.googleapis.com/css2?family=Arimo:wght@400;700&display=swap" rel="stylesheet">
<style>
  :root {
    --bg: #ece7df;
    --card-white: #fbfbfa;
    --teal: #17a5a3;
    --teal-dark: #0f8584;
    --teal-ink: #0c5e5e;
    --gold: #c9bd93;
    --ink: #3a3a3a;
    --muted: #8a8a8a;
  }
  * { box-sizing: border-box; margin: 0; padding: 0; }
  html, body {
    width: 1200px; height: 1023px; overflow: hidden;
    background: var(--bg);
    font-family: "Arimo", Arial, sans-serif;
  }
  .stage { position: relative; width: 1200px; height: 1023px; }

  .card {
    position: absolute;
    width: 620px; height: 354px;
    border-radius: 4px;
    box-shadow: 0 10px 28px rgba(60, 45, 25, .22);
    overflow: hidden;
  }

  /* Front */
  .card-front { left: 70px; top: 90px; background: var(--card-white); }
  .front-brand {
    position: absolute; left: 36px; top: 142px;
    width: 254px;
    display: flex; align-items: center; gap: 10px;
    white-space: nowrap;
  }
  .front-brand .brand-square { width: 18px; height: 18px; }
  .front-brand .brand-name { font-size: 22px; }
  .brand-square { width: 22px; height: 22px; background: var(--teal); flex: none; }
  .brand-name { font-size: 30px; font-weight: 700; color: var(--teal); letter-spacing: .5px; }
  .front-divider {
    position: absolute; left: 308px; top: 60px; width: 1px; height: 190px;
    background: linear-gradient(to bottom, transparent, #444 50%, transparent);
  }
  .contact { position: absolute; left: 334px; top: 92px; }
  .contact-name {
    font-size: 19px; color: var(--teal); letter-spacing: .6px;
    margin-bottom: 20px;
  }
  .contact-line {
    display: flex; align-items: center; gap: 9px;
    font-size: 14px; color: var(--ink); margin-bottom: 9px;
  }
  .contact-line svg { width: 13px; height: 13px; flex: none; }
  .front-rule { position: absolute; left: 0; right: 0; bottom: 32px; height: 4px; background: var(--gold); }
  .front-band { position: absolute; left: 0; right: 0; bottom: 0; height: 32px; background: var(--teal); }

  /* Back */
  .card-back {
    left: 510px; top: 570px;
    background: linear-gradient(135deg, var(--teal) 0%, #14a09f 60%, var(--teal-dark) 100%);
  }
  .back-brand {
    position: absolute; left: 56px; top: 52px;
    display: flex; align-items: center; gap: 12px;
  }
  .back-brand .brand-square { background: #ffffff; }
  .back-brand .brand-name { color: #ffffff; font-size: 38px; }
  .jargon {
    position: absolute; left: 56px; top: 140px;
    list-style: none;
    font-size: 16px; line-height: 22px; letter-spacing: .4px;
    color: var(--teal-ink); text-transform: uppercase;
  }
</style>
</head>
<body>
<main class="stage">
  <section class="card card-front" aria-label="Card front">
    <div class="front-brand">
      <span class="brand-square"></span>
      <span class="brand-name">Vantmoro Studio</span>
    </div>
    <div class="front-divider"></div>
    <div class="contact">
      <p class="contact-name">DORIAN KESWICK</p>
      <p class="contact-line">
        <svg viewBox="0 0 16 16" aria-hidden="true"><path fill="#17a5a3" d="M3 1.5l3 .2 1 3.3-1.8 1.3a9 9 0 0 0 4.5 4.5L11 9l3.3 1 .2 3c-.2 1-1 1.5-2 1.5C6.6 14.2 1.8 9.4 1.5 3.5c0-1 .5-1.8 1.5-2z"/></svg>
        555-013-4827
      </p>
      <p class="contact-line">
        <svg viewBox="0 0 16 16" aria-hidden="true"><rect x="1" y="3" width="14" height="10" fill="#17a5a3"/><path d="M1 3l7 6 7-6" fill="none" stroke="#fff" stroke-width="1.3"/></svg>
        dkeswick@vantmoro.studio
      </p>
      <p class="contact-line">
        <svg viewBox="0 0 16 16" aria-hidden="true"><circle cx="8" cy="8" r="6.5" fill="none" stroke="#17a5a3" stroke-width="1.4"/><path d="M1.5 8h13M8 1.5c-3 3.5-3 9.5 0 13M8 1.5c3 3.5 3 9.5 0 13" fill="none" stroke="#17a5a3" stroke-width="1.1"/></svg>
        www.vantmoro.studio
      </p>
    </div>
    <div class="front-rule"></div>
    <div class="front-band"></div>
  </section>

  <section class="card card-back" aria-label="Card back">
    <div class="back-brand">
      <span class="brand-square"></span>
      <span class="brand-name">Vantmoro Studio</span>
    </div>
    <ul class="jargon">
      <li>Mobile Learning SCORM</li>
      <li>Instructional Design LMS</li>
      <li>MOOCs eLearning HTML5</li>
      <li>How can we help?</li>
      <li>Adult Learning Theory</li>
      <li>Gamification Classroom</li>
      <li>xAPI Blended Learning</li>
    </ul>
  </section>
</main>
</body>
</html>
```